Consumer Finance flyer

This flyer is being developed to help our outside sales people.

Please develop a master template flyer with key bullet points similar to uploaded file.

The main graphic will be replaced as we build out a flyer for each market segment. Example: Healthcare, Dental, Remodeling etc.
so we will keep the bullet point but replace the graphic for each custom vertical industry.

Need flyer to have an editable section at the bottom so the sales person can add their name and phone number and print the flyer.

please incorporate the FundLeafOne logo attached. So it will be branded fundleafone.

Industry/Entity Type

Dental

```html
<!DOCTYPE html>
<html lang="en">
<head>
<meta charset="utf-8">
<title>FundLeafOne – A New Financing Focus</title>
<link rel="stylesheet" href="https://fonts.googleapis.com/css2?family=Delius&family=Open+Sans:wght@700&family=Source+Sans+3:wght@400;600&display=swap">
<style>
  :root {
    --navy: #2f3a58;
    --slate: #5b5c5e;
    --green: #4d8a3c;
    --ink: #2e3340;
    --text: #55585c;
    --paper: #ffffff;
    --photo-light: #eef1f3;
    --photo-skin: #e9c8b4;
    --photo-blue: #4fb6d8;
  }
  * { margin: 0; padding: 0; box-sizing: border-box; }
  html, body {
    width: 908px; height: 1200px; overflow: hidden;
    background: var(--paper);
  }
  .flyer {
    position: relative;
    width: 908px; height: 1200px;
    background: var(--paper);
    font-family: "Source Sans 3", Arial, sans-serif;
    color: var(--text);
    overflow: hidden;
  }
  .shapes { position: absolute; inset: 0; }

  .brand {
    position: absolute; left: 44px; top: 58px;
    display: flex; align-items: center; gap: 14px;
  }
  .brand-name {
    font-size: 44px; font-weight: 400; letter-spacing: 5px;
    color: var(--ink); text-transform: uppercase;
  }
  .brand-dot { width: 18px; height: 18px; border-radius: 50%; background: var(--green); }

  .tagline {
    position: absolute; right: 22px; top: 60px;
    text-align: right; color: var(--paper); line-height: 1;
  }
  .tagline .soft { font-family: "Delius", "Comic Sans MS", cursive; font-size: 62px; display: block; }
  .tagline .strong { font-family: "Open Sans", Arial, sans-serif; font-weight: 700; font-size: 80px; display: block; margin: 2px 0 0; letter-spacing: -1px; }
  .tagline .focus { margin-top: -4px; margin-right: 14px; }

  .headline {
    position: absolute; left: 25px; top: 518px;
    font-family: "Source Sans 3", Arial, sans-serif; font-weight: 400;
    font-size: 51px; line-height: 44px; color: var(--ink);
  }
  .headline span { display: block; white-space: nowrap; }
  .headline .l1 { padding-left: 56px; }
  .headline .l2 { padding-left: 203px; }

  .benefits {
    position: absolute; left: 30px; top: 678px;
    list-style: none; font-size: 16px; line-height: 25.7px;
    text-transform: uppercase; color: var(--text);
  }
  .benefits li { display: flex; align-items: center; gap: 10px; white-space: nowrap; }
  .benefits svg { width: 16px; height: 16px; flex: none; }

  .details {
    position: absolute; left: 378px; top: 676px; width: 300px;
    font-size: 16px; line-height: 21.4px; color: var(--text);
    white-space: nowrap;
  }
  .details p + p { margin-top: 21.4px; }

  .address {
    position: absolute; left: 32px; top: 1092px;
    font-size: 30px; line-height: 38px; color: var(--ink);
    font-style: normal; white-space: nowrap;
  }
  .sales-contact {
    position: absolute; left: 562px; top: 1092px;
    font-size: 30px; line-height: 33px; color: var(--paper);
    white-space: nowrap;
  }
  .sales-contact span { display: block; outline: none; }
</style>
</head>
<body>
<main class="flyer">
  <svg class="shapes" width="908" height="1200" viewBox="0 0 908 1200" aria-hidden="true">
    <polygon class="accent-left" points="0,113 66,113 212,247 42,440 0,440" fill="var(--slate)"/>
    <polygon class="accent-navy" points="570,0 908,0 908,381 481,201" fill="var(--navy)"/>
    <polygon class="accent-right" points="908,720 908,1052 751,883" fill="var(--slate)"/>
    <polygon class="accent-green" points="732,938 908,1102 908,1200 453,1200" fill="var(--green)"/>
  </svg>

  <svg class="shapes" width="908" height="1200" viewBox="0 0 908 1200" role="img" aria-label="Industry photo: a hand holding a stethoscope">
    <defs>
      <linearGradient id="industryPhoto" x1="0" y1="0" x2="1" y2="1">
        <stop offset="0" stop-color="var(--photo-skin)"/>
        <stop offset="0.45" stop-color="var(--photo-light)"/>
        <stop offset="0.8" stop-color="var(--photo-blue)" stop-opacity="0.5"/>
        <stop offset="1" stop-color="var(--paper)" stop-opacity="0"/>
      </linearGradient>
    </defs>
    <polygon points="192,398 408,189 660,339 462,565" fill="url(#industryPhoto)"/>
  </svg>

  <header class="brand">
    <span class="brand-name">FundLeafOne</span>
    <span class="brand-dot"></span>
  </header>

  <h2 class="tagline">
    <span class="soft">a new</span>
    <span class="strong">financing</span>
    <span class="soft focus">focus</span>
  </h2>

  <h1 class="headline">
    <span class="l1">Helping you</span>
    <span class="l2">achieve</span>
    <span>customer satisfaction</span>
  </h1>

  <ul class="benefits">
    <li><svg viewBox="0 0 16 16"><circle cx="8" cy="8" r="7" fill="var(--green)"/><path d="M4.5 8.2l2.3 2.3 4.7-4.8" stroke="#fff" stroke-width="1.8" fill="none"/></svg>Several interest free plans</li>
    <li><svg viewBox="0 0 16 16"><circle cx="8" cy="8" r="7" fill="var(--green)"/><path d="M4.5 8.2l2.3 2.3 4.7-4.8" stroke="#fff" stroke-width="1.8" fill="none"/></svg>0% for 6 to 18 months</li>
    <li><svg viewBox="0 0 16 16"><circle cx="8" cy="8" r="7" fill="var(--green)"/><path d="M4.5 8.2l2.3 2.3 4.7-4.8" stroke="#fff" stroke-width="1.8" fill="none"/></svg>Revolving lines of credit</li>
    <li><svg viewBox="0 0 16 16"><circle cx="8" cy="8" r="7" fill="var(--green)"/><path d="M4.5 8.2l2.3 2.3 4.7-4.8" stroke="#fff" stroke-width="1.8" fill="none"/></svg>Term loans from 2 to 20yrs*</li>
    <li><svg viewBox="0 0 16 16"><circle cx="8" cy="8" r="7" fill="var(--green)"/><path d="M4.5 8.2l2.3 2.3 4.7-4.8" stroke="#fff" stroke-width="1.8" fill="none"/></svg>National lenders compete</li>
    <li><svg viewBox="0 0 16 16"><circle cx="8" cy="8" r="7" fill="var(--green)"/><path d="M4.5 8.2l2.3 2.3 4.7-4.8" stroke="#fff" stroke-width="1.8" fill="none"/></svg>Easy single page app</li>
    <li><svg viewBox="0 0 16 16"><circle cx="8" cy="8" r="7" fill="var(--green)"/><path d="M4.5 8.2l2.3 2.3 4.7-4.8" stroke="#fff" stroke-width="1.8" fill="none"/></svg>Lenient requirements</li>
    <li><svg viewBox="0 0 16 16"><circle cx="8" cy="8" r="7" fill="var(--green)"/><path d="M4.5 8.2l2.3 2.3 4.7-4.8" stroke="#fff" stroke-width="1.8" fill="none"/></svg>No default interest rates</li>
    <li><svg viewBox="0 0 16 16"><circle cx="8" cy="8" r="7" fill="var(--green)"/><path d="M4.5 8.2l2.3 2.3 4.7-4.8" stroke="#fff" stroke-width="1.8" fill="none"/></svg>No prepayment penalties</li>
    <li><svg viewBox="0 0 16 16"><circle cx="8" cy="8" r="7" fill="var(--green)"/><path d="M4.5 8.2l2.3 2.3 4.7-4.8" stroke="#fff" stroke-width="1.8" fill="none"/></svg>May request overnight</li>
    <li><svg viewBox="0 0 16 16"><circle cx="8" cy="8" r="7" fill="var(--green)"/><path d="M4.5 8.2l2.3 2.3 4.7-4.8" stroke="#fff" stroke-width="1.8" fill="none"/></svg>Rates from 6.95%*</li>
    <li><svg viewBox="0 0 16 16"><circle cx="8" cy="8" r="7" fill="var(--green)"/><path d="M4.5 8.2l2.3 2.3 4.7-4.8" stroke="#fff" stroke-width="1.8" fill="none"/></svg>Plus no credit app option</li>
    <li><svg viewBox="0 0 16 16"><circle cx="8" cy="8" r="7" fill="var(--green)"/><path d="M4.5 8.2l2.3 2.3 4.7-4.8" stroke="#fff" stroke-width="1.8" fill="none"/></svg>Approvals in minutes</li>
    <li><svg viewBox="0 0 16 16"><circle cx="8" cy="8" r="7" fill="var(--green)"/><path d="M4.5 8.2l2.3 2.3 4.7-4.8" stroke="#fff" stroke-width="1.8" fill="none"/></svg>May combine offers</li>
    <li><svg viewBox="0 0 16 16"><circle cx="8" cy="8" r="7" fill="var(--green)"/><path d="M4.5 8.2l2.3 2.3 4.7-4.8" stroke="#fff" stroke-width="1.8" fill="none"/></svg>Credit approvals 24 to 48 hrs</li>
  </ul>

  <section class="details">
    <p>Multiple lenders will process your<br>clients with only ONE credit<br>application. We will contact your<br>clients for security and to help<br>expedite the lending process for<br>optimum performance and satisfac-<br>tion. Co borrowers are welcome to<br>help income profile of your clients.<br>This can overcome reservations.</p>
    <p>We provide:<br>Custom application website<br>Online payment calculators.<br>Back office status access.<br>Live assistance.<br>*multiple programs available*</p>
  </section>

  <address class="address">
    Street Name, City Name, State<br>City Zip Code
  </address>

  <footer class="sales-contact">
    <span class="sales-name" contenteditable="true">Sales Persone Name</span>
    <span class="sales-phone" contenteditable="true">Sales Phone #</span>
  </footer>
</main>
</body>
</html>
```